Bus Card for Organic Hydroponic Produce company

We need a business card for a budding new business. We grow 100% organic, 100% hydroponic, 100% GMO free produce for sale in our local area. We need something bold and dynamic, not simple and elegant. We want to catch peoples attention and get them to visit our website to view more information about our products and services. Its difficult to explain on a business card the differences between our produce (tomatoes, cucumbers, peppers, etc...) and the kind they would buy at the local grocer or market. , so we need to push them to the website.
We have been brainstorming names for the company and have a few in mind, so choose whichever speaks most to your artistic flair and propose a card based on that one, or both. #1 "Marrowfield Organics" with a slogan something like....." When merely growing green merely isn't quite enough" OR #2 "Quillbrook Organics" with a slogan similar to...."The cutting edge in cleaner, purer organics" OR #3" "Tandrel Organics" with a slogan similar to: "Building a healthier future for those we leave behind"" OR #4 "Loamwise Path" with a slogan similar to: "Purity by Simplicity"
Eventually we will need assistance with web design, promotional and sales materials, etc. so if you offer those services, please indicate that with the design, though it is NOT necessary to offer any additional services to win this contest. WE will pick the winner solely on the business card we like the most.
We want something that stands out, and especially with the name "Oda's organics", we understand that a creative mind may wander into certain attention getting means that may not be quite within the realm of what we can hand out at our local grocer or farmers market. We definitely are not opposed to a little salacious undertone or allusion to attract attention, but please keep it tasteful if you skirt that grey area.
For our card, we use an online printer that can add foils, special die cuts, double sided cards, 3-d cards (we love these 32 pt cards), transparent or translucent cards and more. We love cards that have some of these things where possible and on all of our other business' cards we get rave reviews from customers about their uniqueness. plumtessa.com has the info on these accents if you wish to view what I am referencing.
So in conclusion, we want a unique, stylish, bold, vivid, 2 sided business card that will really stand out. Just usw a generic phone number and website for now and we will add them as they become available. Please email with any questions! Thanks in advance for your effort and creativity!
Target Market(s)
We are targeting parents who are conceintous of what their children and families are eating. Our target audience are moms, but we don't want to exclude anyone else who chooses to eat more healthy. Our target customer is the same customer that would shop at Brightcart stores or local farmers markets

```html
<!DOCTYPE html>
<html lang="en">
<head>
<meta charset="utf-8">
<title>Garden of Odara Produce – Business Card</title>
<link rel="stylesheet" href="https://fonts.googleapis.com/css2?family=Oswald:wght@300;400;500;600;700&display=swap">
<style>
  :root {
    --green-deep: #0b6b35;
    --blue-band: #1f72bd;
    --red: #e31e24;
    --yellow: #fff200;
    --purple: #7b2a8e;
    --khaki: #a8935a;
    --ink: #1b1b1b;
    --white: #ffffff;
    --bg-top: #f6f7f0;
    --bg-bottom: #9fc4af;
  }
  * { margin: 0; padding: 0; box-sizing: border-box; }
  html, body { width: 683px; height: 1200px; overflow: hidden; }
  body { background: var(--bg-top); }
  .card {
    position: relative;
    width: 683px; height: 1200px; overflow: hidden;
    background: linear-gradient(180deg, var(--bg-top) 0%, #e9efe4 30%, #c6dbcb 70%, var(--bg-bottom) 100%);
    font-family: "Oswald", "Arial Narrow", sans-serif;
  }
  .brand-name {
    position: absolute; top: 18px; left: 34px;
    font-family: "Oswald", "Arial Narrow", sans-serif; font-weight: 700;
    font-size: 90px; line-height: 0.96; color: var(--green-deep);
  }
  .slogan-band {
    position: absolute; top: 298px; left: 0; width: 683px; height: 58px;
    background: var(--blue-band); color: var(--white);
    display: flex; align-items: center; justify-content: center;
    font-size: 33px; font-weight: 300; white-space: nowrap;
  }
  .slogan-band strong { font-weight: 600; margin: 0 8px; }
  .produce-photo {
    position: absolute; top: 356px; left: 225px; width: 458px; height: 651px;
    border-radius: 230px 0 0 200px;
    background: linear-gradient(160deg, #c9452f 0%, #b8503a 18%, #8fb548 42%, #4f8f33 70%, #c7643a 100%);
  }
  .claim-percent {
    position: absolute; top: 362px; left: 36px;
    font-family: "Oswald", Impact, sans-serif; font-weight: 700;
    font-size: 160px; line-height: 1; color: var(--red); letter-spacing: -3px;
  }
  .claim-percent span { font-size: 60px; font-weight: 400; vertical-align: top; position: relative; top: 40px; margin-left: 6px; letter-spacing: 0; }
  .claim-box {
    position: absolute; top: 508px; left: 40px; width: 224px; height: 186px;
    background: var(--yellow);
    border-top: 5px solid var(--blue-band); border-bottom: 5px solid var(--blue-band);
    transform: rotate(-11deg);
    box-shadow: 3px 4px 8px rgba(0,0,0,0.3);
    display: flex; align-items: center; justify-content: center; text-align: center;
    font-family: "Oswald", Impact, sans-serif; font-weight: 600;
    font-size: 35px; line-height: 1.12; color: var(--green-deep);
  }
  .local-badge { position: absolute; top: 714px; left: 94px; width: 140px; height: 140px; }
  .local-badge p {
    position: absolute; inset: 0; display: flex; align-items: center; justify-content: center; text-align: center;
    transform: rotate(-18deg);
    font-family: "Oswald", "Arial Narrow", sans-serif; font-weight: 600;
    font-size: 19px; line-height: 1.15; color: var(--white);
  }
  .headline {
    position: absolute; top: 838px; left: 32px;
    font-family: "Oswald", Impact, sans-serif; font-weight: 700;
    font-size: 90px; line-height: 0.93; color: var(--khaki); letter-spacing: 1px;
  }
  .web-band {
    position: absolute; top: 1007px; left: 0; width: 683px; height: 99px;
    background: var(--green-deep); color: var(--white);
    display: flex; align-items: center; justify-content: center;
    font-family: "Oswald", Impact, sans-serif; font-weight: 600; font-size: 56px;
  }
  .contact {
    position: absolute; top: 1114px; left: 0; width: 683px; text-align: center;
    font-family: "Oswald", "Arial Narrow", sans-serif; font-weight: 400;
    font-size: 23px; line-height: 34px; color: var(--ink); white-space: nowrap;
  }
  .contact .divider { display: inline-block; width: 3px; height: 24px; background: var(--red); vertical-align: -4px; margin: 0 8px; }
</style>
</head>
<body>
  <main class="card">
    <div class="produce-photo" role="img" aria-label="Basket of fresh vegetables: tomatoes, apples, radishes, broccoli, peppers, onions, garlic and carrots"></div>

    <div class="brand-name">Garden of<br>Odara<br>Produce</div>

    <div class="slogan-band">As <strong>Natural</strong> as if <strong>Grown</strong> by <strong>Oda</strong> herself</div>

    <div class="claim-percent">100<span>%</span></div>
    <div class="claim-box">Organic,<br>Hydroponic,<br>GMO free</div>

    <div class="local-badge">
      <svg width="140" height="140" viewBox="-74 -74 148 148" aria-hidden="true">
        <polygon fill="var(--purple)" stroke="#fff" stroke-width="2" points="0,-72 9,-58 24,-68 27,-51 44,-56 40,-39 57,-38 48,-23 64,-16 51,-4 64,8 48,16 58,30 41,33 46,50 29,48 27,65 13,55 4,70 -6,56 -18,68 -22,51 -38,58 -37,41 -54,40 -45,26 -62,18 -49,7 -64,-6 -48,-14 -58,-29 -41,-31 -46,-48 -29,-46 -28,-63 -14,-54 -6,-70"/>
      </svg>
      <p>Available<br>in local<br>area</p>
    </div>

    <div class="headline">HEALTHY<br>EATING</div>

    <div class="web-band">www.OdasOrganics.com</div>

    <div class="contact">
      Phone:555-014-2287<span class="divider"></span>Email: Odasorganics@fernmail.com<br>
      48 Alder Lane, Harrow Bay, VA 23000
    </div>
  </main>
</body>
</html>
```